CBD Boutique Business Card Needed

We are in need of a business card to reflect the direction of our latest products. We are a fully organic company in which our store and products are very heavy in wood and "natural" components. We decided to bring color into one of our brands and immediately knew this is where we needed to go.

We are NOT a cash grab CBD company. We could have done this wrong, slapped a label on a shit product and left it like that. I am passionate about sharing my experience with other veterans and opening a store and making it a comfortable place for others to come and see if they can have the same experience.

Target Market(s)

We are a dual market company. We do have a beauty line that will cover the costs of the majority of our business. But we also heavily cater to veterans and first responders. I am a veteran and this is how I found out about CBD. So the marketing needs to bring in our higher end beauty clientele but also be able to not put off our customers that readily need this.

Contact Information for Business Card

What we are looking for is a light, professional, boutique design that is is neither quite feminine or masculine. Attached is a picture of a store in Portland that we asked our store designer to get her inspiration from. But all natural wood and black outlines are what is mostly in there.

Attached are the following files:

Logo: An AI file with how we have our logo. I do not understand AI and have no idea why the letters are individual. The font is Adam. OLU is the logo and Tonics of Dawn is our tagline.

DC Portrait (front and back) cards I did originally found at a trade show that I absolutely loved...while it is mostly there and I would still be happy with them but it is me pretending to be you. I understand I am not and there is probably a lot wrong that all of you would see instantly and this is why I am here.

Dropper Bottle: This is our final product mock up

Water Color: I am semi flexible here. This water color is slightly different on every level of our brand. The color itself can change...we are not stuck on THIS particular one. If you happen to make a new one that is similar in style and we use it...then I will happily commission you to change the rest on our next product run. I am pretty sure you can use this statement as evidence later . =) .

But seriously, we heavily believe in pay it forward and will work with anyone here that may have a vision bigger than ours. The winner of this contest will get preferential consideration on our marketing materials (need letterhead etc. next, as well as a brochure, and website) so three more projects coming down the pipeline.

Information to use for your mockup is contained on the card images I have included. I would prefer Plant care for body and mind to be more prominent. No where else on the card do we have CBD mentioned.

Font styles to use
Sans Serif

Colors

Designer to choose colors to be used in the design.

Requirements
Must have
• Double Sided
• Front: OLU logo on front of card will be raised embossed. Background is watercolor. One has been provided. Others are up for consideration. If the rest of your design is incredible and I don't like your watercolor I will just ask to swap it.
• Back: Standard information. Not stuck on anything here. I LOVE clean minimal designs. The bleed on the card I provided is a luxury...
• Font for title and OLU is Adam. Everything else I prefer san serif or as clean as possible.
Nice to have
• I Need to incorporate Naturally Nurturing somewhere on the card. Bold but not intrusive.

```html
<!DOCTYPE html>
<html lang="en">
<head>
<meta charset="utf-8">
<title>OLU – Tonics of Dawn business card</title>
<link rel="stylesheet" href="https://fonts.googleapis.com/css2?family=Josefin+Sans:wght@300&family=Montserrat:wght@500;600&display=swap">
<style>
  :root {
    --stage: #e9e7e4;
    --card-front: #cbc7c2;
    --card-back: #ffffff;
    --ink: #1d1d1f;
    --ink-soft: #2b2b2e;
    --wash-teal: #8fcfd3;
    --wash-teal-deep: #6fb8c2;
    --wash-peach: #f1c79a;
    --wash-orange: #e7a874;
  }
  * { box-sizing: border-box; margin: 0; padding: 0; }
  html, body {
    width: 1200px; height: 900px; overflow: hidden;
    background: var(--stage);
  }
  .canvas { position: relative; width: 1200px; height: 900px; }

  .card {
    position: absolute; left: 280px; width: 640px; height: 366px;
    border-radius: 22px; overflow: hidden;
    box-shadow: 0 10px 26px rgba(0,0,0,.16);
  }
  .card--front { top: 70px; background: var(--card-front); }
  .card--back { top: 466px; background: var(--card-back); }

  .front-surface { position: absolute; inset: 0; background: var(--card-front); }

  .brand {
    position: absolute; left: 0; right: 0; top: 96px;
    text-align: center; color: var(--ink);
    font-family: "Josefin Sans", sans-serif; font-weight: 300;
  }
  .brand__name { font-size: 118px; line-height: 1; letter-spacing: 6px; }
  .brand__tagline { margin-top: 8px; font-size: 26px; letter-spacing: 3px; text-transform: uppercase; }

  .watercolor {
    position: absolute; top: 0; right: 0; width: 300px; height: 100%;
    background:
      radial-gradient(ellipse 160px 120px at 70% 18%, var(--wash-orange) 0%, rgba(231,168,116,.55) 45%, rgba(241,199,154,0) 100%),
      radial-gradient(ellipse 150px 140px at 35% 60%, var(--wash-teal-deep) 0%, rgba(143,207,211,.6) 45%, rgba(143,207,211,0) 100%),
      radial-gradient(ellipse 200px 200px at 65% 45%, rgba(241,199,154,.7) 0%, rgba(241,199,154,0) 100%),
      linear-gradient(90deg, rgba(255,255,255,1) 0%, rgba(255,255,255,0) 30%);
    -webkit-mask-image: linear-gradient(180deg, #000 0%, #000 70%, rgba(0,0,0,.2) 95%);
            mask-image: linear-gradient(180deg, #000 0%, #000 70%, rgba(0,0,0,.2) 95%);
  }
  .slogan {
    position: absolute; top: 50%; right: 24px;
    transform: translate(50%, -50%) rotate(-90deg); transform-origin: center;
    white-space: nowrap;
    font-family: "Montserrat", sans-serif; font-weight: 500;
    font-size: 15px; letter-spacing: .6px; color: var(--ink);
    text-transform: uppercase;
  }

  .person { position: absolute; left: 46px; top: 74px; color: var(--ink); }
  .person__name {
    font-family: "Josefin Sans", sans-serif; font-weight: 300;
    font-size: 32px; letter-spacing: 1.5px; text-transform: uppercase;
  }
  .person__role {
    margin-top: 6px;
    font-family: "Montserrat", sans-serif; font-weight: 600;
    font-size: 13px; letter-spacing: .5px;
  }

  .contact {
    position: absolute; left: 46px; bottom: 46px; list-style: none;
    font-family: "Montserrat", sans-serif; font-weight: 500;
    font-size: 16px; color: var(--ink-soft); text-transform: uppercase;
  }
  .contact__item { display: flex; align-items: flex-start; gap: 10px; line-height: 21px; }
  .contact__item--address { margin-bottom: 22px; }
  .contact__icon { width: 14px; height: 14px; margin-top: 3px; flex: none; fill: var(--ink-soft); }
</style>
</head>
<body>
<main class="canvas">

  <section class="card card--front" aria-label="Card front">
    <div class="front-surface" role="img" aria-label="Faint geometric tile pattern on warm grey"></div>
    <div class="brand">
      <div class="brand__name">OLU</div>
      <div class="brand__tagline">Tonics of Dawn</div>
    </div>
  </section>

  <section class="card card--back" aria-label="Card back">
    <div class="watercolor" role="img" aria-label="Teal and peach watercolour wash with faint geometric tile pattern"></div>
    <p class="slogan">Plant care for body and mind</p>

    <div class="person">
      <h1 class="person__name">Nora Whitfield</h1>
      <p class="person__role">OWNER/CEO</p>
    </div>

    <ul class="contact">
      <li class="contact__item contact__item--address">
        <svg class="contact__icon" viewBox="0 0 24 24" aria-hidden="true"><path d="M12 1a8 8 0 0 0-8 8c0 6 8 14 8 14s8-8 8-14a8 8 0 0 0-8-8zm0 11a3 3 0 1 1 0-6 3 3 0 0 1 0 6z"/></svg>
        <span>2417 W Linden Vale Rd<br>Harlow, AZ 85014</span>
      </li>
      <li class="contact__item">
        <svg class="contact__icon" viewBox="0 0 24 24" aria-hidden="true"><path d="M6.6 10.8a15.2 15.2 0 0 0 6.6 6.6l2.2-2.2a1 1 0 0 1 1-.25 11.4 11.4 0 0 0 3.6.57 1 1 0 0 1 1 1V20a1 1 0 0 1-1 1A17 17 0 0 1 3 4a1 1 0 0 1 1-1h3.5a1 1 0 0 1 1 1c0 1.25.2 2.45.57 3.6a1 1 0 0 1-.25 1z"/></svg>
        <span>555 214 0386</span>
      </li>
      <li class="contact__item">
        <svg class="contact__icon" viewBox="0 0 24 24" aria-hidden="true"><path d="M2 5h20v14H2z M2 5l10 8 10-8" stroke="#fff" stroke-width="1.6"/></svg>
        <span>hello@olu.shop</span>
      </li>
      <li class="contact__item">
        <svg class="contact__icon" viewBox="0 0 24 24" aria-hidden="true"><circle cx="12" cy="12" r="11"/><path d="M1 12h22M12 1c-4 4-4 18 0 22M12 1c4 4 4 18 0 22M3 7h18M3 17h18" stroke="#fff" stroke-width="1.3" fill="none"/></svg>
        <span>www.olu.shop</span>
      </li>
    </ul>
  </section>

</main>
</body>
</html>
```